VELORA5 SPORTS NETWORK

design a website that will be a companion to a sports network that features womens sports and fitness content.
With the goal of promoting and empowering female athleticism, Velora5tv.example will be the online network that connects female sports fans to the sports they love and follow. The site aims to raise the level of awareness of women in sports by providing comprehensive sports coverage, spotlighting outstanding achievements, and working with sporting associations on advocacy issues and empowering programs.
Updates
I would like to have all entry by Sunday June 8 2014 thank you
please use actual script not lorem ipsum
thank you
Deadline winding down, added new pictures to file
Target Market(s)
our target market is females 18-54, whom love womens sports and ftiness
Industry/Entity Type
Fitness
Font styles to use
Requirements
Must have
- Attributes of the website:
1. Large Photos: to accompany current stories
2. Colorful: Highlight Velora5’s officials colors
3. News Area: recent news items on the home page and achieved news stories
4. Featured Content area: Headline news, athlete spotlights and issues
5. Streaming content: to accompany news and featured content
6. Advertiser links: to purchase merchandise
7. Real-time scores of live events
8. Blog
9. Monthly newsletter
10. Athlete profile page
11. Model close to QRTV
Nice to have
- Velora5tv.example will offer value-added service that will entitle customers to gain access to online streaming services provided by Velora5, which delivers both live streams and on-demand replays of global women’s sports events to sports fans in U.S. and abroad. This service will be subscription based for a modest monthly fee. Content will be available across multiple platforms and cloud based. New subscriber will get first 30 days free.
Content will include:
1. Live sports events
2. On-demand and premium content
3. Fan-generated Content

```html
<!DOCTYPE html>
<html lang="en">
<head>
<meta charset="utf-8">
<title>Velora5 Sports Network</title>
<link href="https://fonts.googleapis.com/css2?family=Oswald:wght@400;500&family=Open+Sans:wght@400;600&display=swap" rel="stylesheet">
<style>
:root{
  --red:#e2432c;
  --red-dark:#d8342a;
  --purple:#9c5bc9;
  --page:#efefef;
  --card:#ffffff;
  --line:#e4e4e4;
  --ink:#333333;
  --muted:#8a8a8a;
  --menu-grey:#9a9a9a;
}
*{box-sizing:border-box;margin:0;padding:0}
html,body{width:846px;height:1200px;overflow:hidden}
body{background:var(--page);font-family:"Open Sans",sans-serif;color:var(--ink);position:relative}
h1,h2,h3{font-weight:400}
.head{font-family:"Oswald",sans-serif;font-weight:400}
ul{list-style:none}

/* header */
.site-header{position:absolute;left:0;top:0;width:846px;height:95px;background:#fff}
.brand{position:absolute;left:26px;top:34px;display:flex;align-items:center;gap:6px}
.brand-mark{width:14px;height:14px;background:var(--red)}
.brand-name{font-family:"Oswald",sans-serif;font-size:16px;color:var(--red);line-height:1.1}
.brand-name small{display:block;font-size:7px;letter-spacing:.5px}
.social{position:absolute;right:22px;top:18px;display:flex;gap:30px}
.social span{width:9px;height:9px;border-radius:50%;background:#444;display:block}
.main-nav{position:absolute;left:342px;top:52px;display:flex}
.main-nav a{font-family:"Oswald",sans-serif;font-size:19px;color:#444;text-decoration:none;margin-right:40px;line-height:26px}
.main-nav a.active{color:var(--red)}
.nav-underline{position:absolute;left:342px;top:91px;width:164px;height:3px;background:var(--red)}
.nav-caret{position:absolute;left:419px;top:85px;width:0;height:0;border-left:5px solid transparent;border-right:5px solid transparent;border-bottom:6px solid var(--red)}
.nav-btn{position:absolute;top:48px;width:32px;height:32px;background:#d7d7d7;display:flex;align-items:center;justify-content:center}

/* top band */
.card{position:absolute;background:var(--card)}
.recent-top{left:15px;top:105px;width:162px;height:258px}
.recent-top h2{font-size:17px;text-align:center;margin-top:10px;color:#333}
.recent-top .bar{width:100px;height:2px;background:var(--red);margin:2px auto 0}
.thumb{position:absolute;left:9px;width:143px;height:75px}
.thumb-cap{position:absolute;left:9px;width:143px;font-size:9px;color:var(--muted);text-align:center;line-height:11px}

.slider{position:absolute;left:188px;top:105px;width:446px;height:258px;background:linear-gradient(180deg,#dfe9ea,#c9d6d4 60%,#b9b39a)}
.slide-arrow{position:absolute;top:114px;width:24px;height:36px;background:#777;opacity:.85;display:flex;align-items:center;justify-content:center}
.slide-caption{position:absolute;left:12px;top:155px;width:434px;height:103px;background:rgba(255,255,255,.93);padding:12px 30px 0 26px}
.slide-caption h1{font-family:"Oswald",sans-serif;font-size:19px;line-height:24px;color:var(--red)}
.slide-caption p{font-size:9px;line-height:11px;margin-top:7px;color:#333}

.headlines{left:646px;top:105px;width:183px;height:258px}
.headlines h2{height:36px;background:var(--purple);color:#fff;text-align:center;font-size:17px;line-height:36px}
.headlines li{font-size:8.5px;line-height:11px;color:var(--muted);padding:9px 16px;border-bottom:1px solid var(--line);height:40px}

/* main */
.main{left:15px;top:372px;width:814px;height:713px}
.cat-menu{position:absolute;left:10px;top:13px;width:163px;height:283px;border:1px solid var(--line)}
.cat-menu li{font-family:"Oswald",sans-serif;font-size:13px;color:#666;height:32px;line-height:32px;padding-left:19px;border-bottom:1px solid var(--line)}
.cat-menu li.active{background:var(--menu-grey);color:#fff;height:36px;line-height:36px}
.cat-menu li:last-child{border-bottom:none}

.feature{position:absolute;left:184px;top:20px;width:425px}
.feature h2{font-size:16px;color:#555;padding-bottom:4px;border-bottom:2px solid var(--red)}
.video{position:relative;margin-top:12px;width:425px;height:195px;background:linear-gradient(135deg,#8aa25c,#c8c7a9 55%,#e9e2d6)}
.controls{position:absolute;left:0;bottom:0;width:425px;height:26px;background:rgba(30,30,30,.8);display:flex;align-items:center;padding:0 10px;gap:8px;color:#fff;font-size:7px}
.track{flex:1;height:3px;background:#555;position:relative}
.track i{position:absolute;left:0;top:0;height:3px;width:70%;background:var(--red)}
.track b{position:absolute;left:70%;top:-3px;width:9px;height:9px;border-radius:50%;background:#ddd}
.feature p{font-size:9px;line-height:13.5px;color:#777;margin-top:10px}
.rule{position:absolute;left:10px;width:600px;border-top:1px dotted #ccc}

.post{position:absolute;left:10px;width:600px;height:150px}
.post-img{position:absolute;left:0;top:0;width:192px;height:145px;background:linear-gradient(135deg,#f3efe9,#b6c59a 60%,#6d8a4a)}
.post-badge{position:absolute;left:186px;top:115px;width:35px;height:34px;background:var(--red);color:#fff;font-size:11px;text-align:center;line-height:12px;padding-top:5px}
.post h3{position:absolute;left:208px;top:4px;width:392px;text-align:center;font-family:"Oswald",sans-serif;font-size:21px;color:#333}
.post .meta{position:absolute;left:208px;top:42px;width:392px;text-align:center;font-size:9.5px;color:var(--muted)}
.post .meta-bar{position:absolute;left:344px;top:64px;width:148px;height:2px;background:var(--red)}
.post p{position:absolute;left:222px;top:86px;width:376px;font-size:9px;line-height:14px;color:#777}

.sidebar{position:absolute;left:622px;top:33px;width:183px;height:660px;border:1px solid #f0c6c0;padding:3px}
.sidebar-inner{position:relative;width:100%;height:100%;border:1px solid #f3d6d2}
.side-h{font-family:"Oswald",sans-serif;font-weight:400;font-size:19px;line-height:24px;color:#444;text-align:center}
.side-bar{width:100px;height:2px;background:var(--red);margin:6px auto 0}
.side-list li{position:relative;padding-left:12px;color:#555;white-space:nowrap}
.side-list li::before{content:"";position:absolute;left:0;top:5px;width:4px;height:4px;background:var(--red)}
.ad{position:absolute;left:0;bottom:0;width:100%;height:157px;background:linear-gradient(180deg,#dadada,#efefef 55%,#d9d9d9);text-align:center;padding-top:40px}
.ad strong{font-family:"Oswald",sans-serif;font-weight:400;display:block;color:var(--red-dark);font-size:27px;line-height:32px}
.ad span{font-size:12px;color:#444}

/* footer */
.site-footer{position:absolute;left:15px;top:1100px;width:814px;height:86px;border-top:2px solid #666;border-bottom:2px solid #666;text-align:center;padding-top:25px;font-size:12.5px;line-height:15px;color:var(--muted)}
</style>
</head>
<body>

<header class="site-header">
  <div class="brand">
    <span class="brand-mark"></span>
    <span class="brand-name">VELORA5<small>SPORTS NETWORK</small></span>
  </div>
  <div class="social" aria-label="Social links"><span></span><span></span><span></span><span></span><span></span></div>
  <nav class="main-nav">
    <a class="active" href="#">NEWS &amp; COMMENTARY</a>
    <a href="#">ATHLETE'S LIFE</a>
    <a href="#">IN ACTION</a>
  </nav>
  <div class="nav-caret"></div>
  <div class="nav-underline"></div>
  <div class="nav-btn" style="left:762px" aria-label="Play">
    <svg width="14" height="14" viewBox="0 0 14 14"><path d="M3 1 L13 7 L3 13 Z" fill="#fff"/></svg>
  </div>
  <div class="nav-btn" style="left:796px" aria-label="Search">
    <svg width="16" height="16" viewBox="0 0 16 16"><circle cx="6.5" cy="6.5" r="5" stroke="#fff" stroke-width="2" fill="none"/><line x1="10" y1="10" x2="15" y2="15" stroke="#fff" stroke-width="2"/></svg>
  </div>
</header>

<section class="card recent-top">
  <h2 class="head">Most Recent</h2>
  <div class="bar"></div>
  <div class="thumb" role="img" aria-label="Photo of golfers on a green course" style="top:42px;background:linear-gradient(180deg,#cfe1f0,#7fa05a)"></div>
  <div class="thumb-cap" style="top:122px">Owen Pratt and Leo Brandt discuss the five biggest sto-</div>
  <div class="thumb" role="img" aria-label="Photo of a tennis player swinging a racket" style="top:150px;background:linear-gradient(180deg,#4f95c8,#8cc3e6)"></div>
  <div class="thumb-cap" style="top:230px">Owen Pratt and Leo Brandt discuss the five biggest sto-</div>
</section>

<section class="slider" role="img" aria-label="Photo of two tennis players talking on court">
  <div class="slide-arrow" style="left:0">
    <svg width="10" height="18" viewBox="0 0 10 18"><path d="M9 1 L1 9 L9 17" stroke="#fff" stroke-width="1.5" fill="none"/></svg>
  </div>
  <div class="slide-arrow" style="right:0">
    <svg width="10" height="18" viewBox="0 0 10 18"><path d="M1 1 L9 9 L1 17" stroke="#fff" stroke-width="1.5" fill="none"/></svg>
  </div>
  <div class="slide-caption">
    <h1>Marlowe lifts Tempest over winless Volt June Ardent and Keisha Dunmore added 11 points</h1>
    <p>Northvale and Eastbrook, the teams vying for softball's national championship, share more than their membership in the SCL.</p>
  </div>
</section>

<aside class="card headlines">
  <h2 class="head">Headline news</h2>
  <ul>
    <li>Dana Holloway and Rita Calvo preview the Women's</li>
    <li>Dana Holloway and Rita Calvo pre-view the Women's</li>
    <li>Dana Holloway and Rita Calvo pre-view the Women's</li>
    <li>Dana Holloway and Rita Calvo pre-view the Women's</li>
    <li style="border-bottom:none">Dana Holloway and Rita Calvo pre-view the Women's</li>
  </ul>
</aside>

<main class="card main">
  <ul class="cat-menu">
    <li class="active">Most Recent</li>
    <li>Spelling Bee</li>
    <li>Tennis</li>
    <li>Softball</li>
    <li>Soccer</li>
    <li>College Sports</li>
    <li>Golf</li>
    <li>Olympic Sport</li>
  </ul>

  <article class="feature">
    <h2 class="head">5 THINGS WE LEARNED: PARIS CLAY OPEN DAY 8</h2>
    <div class="video" role="img" aria-label="Video still of a smiling tennis player holding a racket">
      <div class="controls">
        <svg width="9" height="10" viewBox="0 0 9 10"><path d="M0 0 L9 5 L0 10 Z" fill="#fff"/></svg>
        <span>00:26</span>
        <div class="track"><i></i><b></b></div>
        <span>00:35</span>
        <svg width="10" height="10" viewBox="0 0 10 10"><path d="M0 3 H3 L6 0 V10 L3 7 H0 Z" fill="#fff"/></svg>
        <div style="width:24px;height:3px;background:var(--red)"></div>
        <svg width="10" height="10" viewBox="0 0 10 10" fill="none" stroke="#fff"><path d="M0 3 V0 H3 M7 0 H10 V3 M10 7 V10 H7 M3 10 H0 V7"/></svg>
      </div>
    </div>
    <p>Owen Pratt and Leo Brandt discuss the five biggest storylines from Day 8 of the Paris Clay Open, including Anton Vell's loss and Marek Dolan becoming the first Canadian man in the Open era to reach the quarterfinals of a Grand Slam.</p>
  </article>

  <div class="rule" style="top:316px"></div>

  <article class="post" style="top:336px">
    <div class="post-img" role="img" aria-label="Photo of smiling women golfers on a course"></div>
    <div class="post-badge">&#9650;<br>4</div>
    <h3>MAURIS IACULIS PORTTITOR</h3>
    <div class="meta">PAOLO VENTRI &nbsp;/&nbsp; NEWS &nbsp;/&nbsp; NO RESPONSES &nbsp;/&nbsp; APRIL 8, 2014</div>
    <div class="meta-bar"></div>
    <p>Lorem ipsum dolor sit amet, consectetur adipiscing elit. Nullam in dui mauris. Vivamus hendrerit arcu sed erat molestie vehicula. Sed auctor neque eu tellus rhoncus ut eleifend nibh porttitor. Ut in nulla enim. Phasellus molestie magna non est bibendum non venenatis nisl tempor. Suspendisse dictum feugiat nisl ut dapibus. Mauris iaculis. In Pel-lentesque Faucibus Vestibulum....</p>
  </article>

  <div class="rule" style="top:504px"></div>

  <article class="post" style="top:526px">
    <div class="post-img" role="img" aria-label="Photo of smiling women golfers on a course"></div>
    <div class="post-badge">&#9650;<br>4</div>
    <h3>MAURIS IACULIS PORTTITOR</h3>
    <div class="meta">PAOLO VENTRI &nbsp;/&nbsp; NEWS &nbsp;/&nbsp; NO RESPONSES &nbsp;/&nbsp; APRIL 8, 2014</div>
    <div class="meta-bar"></div>
    <p>Lorem ipsum dolor sit amet, consectetur adipiscing elit. Nullam in dui mauris. Vivamus hendrerit arcu sed erat molestie vehicula. Sed auctor neque eu tellus rhoncus ut eleifend nibh porttitor. Ut in nulla enim. Phasellus molestie magna non est bibendum non venenatis nisl tempor. Suspendisse dictum feugiat nisl ut dapibus. Mauris iaculis. In Pel-lentesque Faucibus Vestibulum....</p>
  </article>

  <div class="rule" style="top:693px"></div>

  <aside class="sidebar">
    <div class="sidebar-inner">
      <h3 class="side-h" style="margin-top:20px">Subscribes &amp;<br>Get These Services</h3>
      <div class="side-bar"></div>
      <ul class="side-list" style="margin:18px 0 0 28px;font-size:11px;line-height:12px">
        <li style="margin-bottom:6px">Live sports events</li>
        <li style="margin-bottom:6px">On-demand &amp; premium<br>content</li>
        <li>Fan-generated Content</li>
      </ul>
      <p style="margin:9px 0 0 28px;font-size:8.5px;line-height:11px;color:#777;width:130px">New subscriber will get first 30 days free.</p>
      <h3 class="side-h" style="margin-top:50px">Athlete Spotlights &amp;<br>Issues</h3>
      <div class="side-bar"></div>
      <ul class="side-list" style="margin:24px 0 0 16px;font-size:8px;line-height:11px;letter-spacing:-.1px">
        <li style="margin-bottom:7.7px">Images in a post</li>
        <li style="margin-bottom:7.7px">Best Family Vacation Destinations</li>
        <li style="margin-bottom:7.7px">Old Style Magazine Theme</li>
        <li style="margin-bottom:7.7px">Suspendisse Dictum Feugiat Nisl</li>
        <li style="margin-bottom:7.7px">Video post format: Skyvane</li>
        <li style="margin-bottom:7.7px">Old Style Magazine Theme</li>
        <li style="margin-bottom:7.7px">Suspendisse Dictum Feugiat Nisl</li>
        <li>Video post format: Skyvane</li>
      </ul>
      <div class="ad">
        <strong>purchase<br>merchandise</strong>
        <span>Advertising Here</span>
      </div>
    </div>
  </aside>
</main>

<footer class="site-footer">
  Help | Press | Advertise on &nbsp;| Sales Media Kit | Interest-Based Ads | Report a Bug | Corrections | Contact Us<br>
  Site Map &nbsp;Terms of Use and Privacy Policy and Safety Information / Your &nbsp;Privacy Rights are applicable to you. All rights reserved.
</footer>

</body>
</html>
```